Consulting Company needs business card design

We need a business card design for a new consulting and business solutions company based in Bermuda called Corvale Partners Limited. Looking for a double sided business card with one side only including the company logo thats attached and the other including contact information. Logo contains blue and turquoise colors and is fine to be on both sides of the card.
Contact Information for Business Card
Corvale Partners Limited
P.O. Box HM318
Devonshire DV BX
Bermuda
Name: Marcus Pellegrin
Position: Director
Telephone: 1 441 733 4906
Email: mpellegrin@corvale.example
Website: www.corvale.example

```html
<!DOCTYPE html>
<html lang="en">
<head>
<meta charset="utf-8">
<title>Corvale Partners Limited – Business Card</title>
<link rel="stylesheet" href="https://fonts.googleapis.com/css2?family=Roboto:wght@400;500;700&display=swap">
<style>
  :root {
    --backdrop: #3a3a3a;
    --card: #232323;
    --ink-light: #f2f2f2;
    --ink-soft: #c9c9c9;
    --accent: #1fa8bd;
    --divider: #e6e6e6;
  }
  * { margin: 0; padding: 0; box-sizing: border-box; }
  html, body { width: 1200px; height: 900px; overflow: hidden; }
  body {
    background: var(--backdrop);
    font-family: "Roboto", Arial, sans-serif;
    display: flex;
    flex-direction: column;
    align-items: center;
    justify-content: center;
    gap: 40px;
  }
  .card {
    width: 665px;
    height: 380px;
    background: var(--card);
    box-shadow: 0 10px 30px rgba(0,0,0,0.45);
    display: flex;
    flex-direction: column;
    align-items: center;
    justify-content: center;
    text-align: center;
  }
  .brand {
    display: flex;
    align-items: center;
    gap: 16px;
  }
  .brand-dot {
    width: 22px;
    height: 22px;
    border-radius: 50%;
    background: var(--ink-soft);
  }
  .brand-name {
    font-weight: 500;
    font-size: 34px;
    letter-spacing: 3px;
    text-transform: uppercase;
    color: var(--ink-soft);
  }
  .person-name {
    font-weight: 700;
    font-size: 30px;
    color: var(--accent);
    letter-spacing: 0.5px;
  }
  .person-role {
    font-size: 19px;
    color: var(--ink-light);
    margin-top: 2px;
  }
  .divider {
    width: 46px;
    height: 2px;
    background: var(--divider);
    margin: 26px 0 24px;
  }
  .contact-list {
    list-style: none;
    display: flex;
    flex-direction: column;
    align-items: center;
    gap: 4px;
    font-size: 19px;
    color: var(--ink-light);
  }
  .contact-item { display: flex; align-items: center; gap: 8px; }
  .contact-icon { width: 18px; height: 18px; flex: none; }
  .accent { color: var(--accent); }
  .address {
    margin-top: 10px;
    font-size: 19px;
    color: var(--ink-light);
  }
</style>
</head>
<body>
  <section class="card card-front">
    <div class="brand">
      <span class="brand-dot"></span>
      <span class="brand-name">Corvale Partners Limited</span>
    </div>
  </section>

  <section class="card card-back">
    <h1 class="person-name">Marcus Pellegrin</h1>
    <p class="person-role">Director</p>
    <div class="divider"></div>
    <ul class="contact-list">
      <li class="contact-item">
        <svg class="contact-icon" viewBox="0 0 24 24" aria-hidden="true"><path fill="#1fa8bd" d="M6.6 10.8a15.1 15.1 0 0 0 6.6 6.6l2.2-2.2c.3-.3.7-.4 1-.2 1.1.4 2.3.6 3.6.6.6 0 1 .4 1 1V20c0 .6-.4 1-1 1A17 17 0 0 1 3 4c0-.6.4-1 1-1h3.5c.6 0 1 .4 1 1 0 1.3.2 2.5.6 3.6.1.3 0 .7-.2 1z"/></svg>
        <span>1 441 733 4906</span>
      </li>
      <li class="contact-item">
        <svg class="contact-icon" viewBox="0 0 24 24" aria-hidden="true"><rect x="2.5" y="5" width="19" height="14" fill="none" stroke="#1fa8bd" stroke-width="1.6"/><path d="M2.5 5l9.5 8 9.5-8" fill="none" stroke="#1fa8bd" stroke-width="1.6"/></svg>
        <span>mpellegrin@corvale.example</span>
      </li>
      <li class="contact-item">
        <svg class="contact-icon" viewBox="0 0 24 24" aria-hidden="true"><g fill="none" stroke="#1fa8bd" stroke-width="1.6"><circle cx="12" cy="12" r="9.5"/><ellipse cx="12" cy="12" rx="4.2" ry="9.5"/><path d="M2.5 12h19M4 7h16M4 17h16"/></g></svg>
        <span>www.<span class="accent">corvale</span>.example</span>
      </li>
    </ul>
    <p class="address">P.O. Box HM318, Devonshire DV BX, Bermuda</p>
  </section>
</body>
</html>
```